Website design: professional but personally
Needs:
Our visitors are mostly people that look for a IT or technical jobs, but our customers are also visiting our website.
Core values are: personally, professional, ambition, growth, personal development
Terms that we think of are:
Professional, but personal (we ware no trading company, but we do have internation customers)
People
IT (jobs)
Engineering (jobs)

```html
<!DOCTYPE html>
<html lang="nl">
<head>
<meta charset="utf-8">
<title>WerkKring – Zoek de perfecte baan</title>
<link href="https://fonts.googleapis.com/css2?family=Poppins:wght@300;400;500;600;700&display=swap" rel="stylesheet">
<style>
:root{
  --green:#8dc63f;
  --green-dark:#76ad2c;
  --blue:#3b7ddd;
  --blue-dark:#2d66bd;
  --ink:#3a3a3a;
  --muted:#9a9a9a;
  --soft:#ececec;
  --line:#e4e4e4;
  --footer:#2a2a2a;
  --white:#ffffff;
}
*{box-sizing:border-box;margin:0;padding:0}
html,body{width:1200px;height:2620px;overflow:hidden}
body{position:relative;background:var(--white);font-family:'Poppins',sans-serif;color:var(--ink)}
.abs{position:absolute}

/* navigation */
.site-nav{left:0;top:0;width:1200px;height:64px;background:var(--white)}
.nav-link{position:absolute;top:22px;font-size:13px;font-weight:600;letter-spacing:.5px;color:#444;text-transform:uppercase}
.nav-link.is-active{background:var(--green);color:var(--white);padding:2px 7px;top:20px;font-size:12px}
.brand{position:absolute;left:530px;top:14px;width:142px;text-align:center;font-size:26px;font-weight:700;letter-spacing:1px;color:#333}
.nav-burger{position:absolute;left:944px;top:25px;width:14px}
.nav-burger span{display:block;height:2px;background:#444;margin-bottom:3px}

/* hero */
.hero{left:0;top:64px;width:1200px;height:316px;background:linear-gradient(100deg,#0f2a4d 0%,#1f4f86 45%,#173a63 70%,#0c2038 100%)}
.hero-title{left:0;top:192px;width:1200px;text-align:center;color:var(--green);font-size:16px;font-weight:700;letter-spacing:.5px;text-transform:uppercase}
.search-field{top:246px;height:38px;background:var(--blue);color:var(--white);font-size:12px;font-weight:600;text-transform:uppercase;display:flex;align-items:center}
.search-query{left:290px;width:286px;padding-left:14px;gap:14px}
.search-branch{left:580px;width:160px;padding:0 14px;justify-content:space-between}
.search-submit{left:746px;width:162px;background:var(--green);justify-content:center}

/* section titles */
.section-title{left:0;width:1200px;text-align:center;color:var(--green);font-size:15px;font-weight:700;text-transform:uppercase;letter-spacing:.3px}

/* featured jobs */
.featured{left:0;top:380px;width:1200px;height:344px;background:var(--soft)}
.job-card{top:450px;width:184px;height:196px;background:var(--white);padding:12px 14px 0;box-shadow:0 1px 3px rgba(0,0,0,.08)}
.job-title{font-size:11px;font-weight:600;text-transform:uppercase;color:#555;line-height:1.3}
.job-title.is-tagged{background:var(--green);color:var(--white);display:inline;font-size:9.5px;line-height:1.5}
.job-badge{position:absolute;right:14px;top:12px;font-size:8px;font-weight:700;color:var(--blue);text-transform:uppercase}
.job-place{font-size:8px;color:#bbb;text-align:right;margin-top:2px;border-bottom:1px solid var(--line);padding-bottom:4px;text-transform:uppercase}
.job-text{font-size:9px;line-height:1.6;color:#777;margin-top:6px;height:130px;overflow:hidden}
.job-more{top:640px;height:22px;width:120px}
.btn-more{position:absolute;left:0;top:0;width:108px;height:22px;background:var(--green);color:var(--white);font-size:10px;font-weight:600;text-transform:uppercase;text-align:center;line-height:22px}
.btn-arrow{position:absolute;right:0;top:2px;width:18px;height:18px;background:var(--blue);transform:rotate(45deg)}
.btn-arrow::after{content:"";position:absolute;left:5px;top:6px;width:5px;height:5px;border-top:1.5px solid #fff;border-right:1.5px solid #fff}
.all-jobs{left:538px;top:708px;width:124px;height:34px;background:var(--blue);color:var(--white);font-size:11px;font-weight:600;text-align:center;line-height:34px;text-transform:uppercase;box-shadow:0 2px 4px rgba(0,0,0,.2)}

/* about */
.photo{box-shadow:0 3px 8px rgba(0,0,0,.25)}
.photo-tech{left:208px;top:884px;width:104px;height:176px;background:linear-gradient(135deg,#1a4f8a,#4da0d8 60%,#b8d8ee)}
.photo-main{left:306px;top:864px;width:188px;height:312px;background:linear-gradient(160deg,#e8eef2,#c9d3da 50%,#7a8590)}
.photo-side{left:492px;top:978px;width:104px;height:172px;background:linear-gradient(160deg,#dfe3e6,#9aa3ab 60%,#3f4750)}
.about-text{left:622px;top:874px;width:380px;font-size:10.5px;line-height:1.62;color:#9a9a9a}
.about-text p+p{margin-top:16px}

/* newsletter */
.newsletter{left:0;top:1268px;width:1200px;height:196px;background:linear-gradient(90deg,#c9b59d 0%,#a9a49a 35%,#8b959c 65%,#7f8a93 100%)}
.newsletter-shade{left:0;top:1268px;width:1200px;height:196px;background:rgba(60,60,60,.35)}
.newsletter-title{left:0;top:1326px;width:1200px;text-align:center;color:var(--white);font-size:14px;font-weight:700;text-transform:uppercase}
.newsletter-input{left:372px;top:1374px;width:326px;height:32px;background:var(--green);color:var(--white);font-size:11px;font-weight:600;line-height:32px;padding-left:14px;text-transform:uppercase}
.newsletter-submit{left:702px;top:1374px;width:118px;height:32px}
.newsletter-submit .btn-more{width:104px;height:32px;line-height:32px}
.newsletter-submit .btn-arrow{width:22px;height:22px;top:5px;right:2px}
.newsletter-submit .btn-arrow::after{left:6px;top:8px}

/* teaser */
.teaser-col{top:1560px;width:384px;height:90px;font-size:8.5px;line-height:18px;color:#555;overflow:hidden}

/* team */
.team-band{left:0;top:1716px;width:1200px;height:134px;background:var(--green)}
.member{width:122px;height:122px;transform:rotate(45deg);border:4px solid var(--white);box-shadow:0 2px 6px rgba(0,0,0,.2)}
.member-dark{background:#2e2e2e}
.member-photo-a{background:linear-gradient(180deg,#f3f3f3,#c7c7c7 55%,#3a3f46)}
.member-photo-b{background:linear-gradient(180deg,#f5f5f5,#d3c7bd 55%,#2c2c2c)}
.member-name{left:236px;top:1822px;width:128px;text-align:center;color:var(--white);font-size:11px;font-weight:600;letter-spacing:2px;text-transform:uppercase}
.member-role{left:236px;top:1840px;width:128px;text-align:center;color:#bbb;font-size:8px;letter-spacing:2px;text-transform:uppercase}
.social-dot{width:16px;height:16px;border-radius:50%;background:#555}
.member-socials{left:272px;top:1890px;display:flex;gap:6px}
.member-socials .social-dot:last-child{background:var(--blue)}

/* partners */
.partner{width:96px;height:96px}
.partner-frame{position:absolute;inset:0;border:1px solid #e8e8e8;transform:rotate(45deg);background:var(--white)}
.partner-name{position:absolute;left:-20px;top:36px;width:136px;text-align:center;font-size:17px;font-weight:600;color:#333}

/* footer */
.footer{left:0;top:2318px;width:1200px;height:302px;background:var(--footer)}
.footer-col{top:2402px;width:160px;color:#d8d8d8}
.footer-col h3{font-size:11.5px;font-weight:600;color:var(--white);margin-bottom:22px}
.footer-col p{font-size:9.5px;line-height:1.9}
.footer-col .underline{text-decoration:underline}
.footer-socials{display:flex;gap:12px;margin-top:14px}
.footer-socials .social-dot{background:#444}
</style>
</head>
<body>

<nav class="abs site-nav" aria-label="Hoofdmenu">
  <span class="nav-link is-active" style="left:208px">Home</span>
  <span class="nav-link" style="left:298px">Over ons</span>
  <span class="nav-link" style="left:412px">Kandidaten</span>
  <span class="brand">WerkKring</span>
  <span class="nav-link" style="left:712px">Vacatures</span>
  <span class="nav-link" style="left:836px">Contact</span>
  <span class="nav-burger"><span></span><span></span><span></span></span>
</nav>

<header>
  <div class="abs hero" role="img" aria-label="Foto van een hand die een persoon kiest uit een rij mensen-iconen, in donkerblauwe tinten"></div>
  <h1 class="abs hero-title">Zoek de perfecte baan die bij mij past</h1>
  <div class="abs search-field search-query">
    <svg width="14" height="14" viewBox="0 0 14 14"><circle cx="6" cy="6" r="4.5" fill="none" stroke="#fff" stroke-width="1.8"/><line x1="9.3" y1="9.3" x2="13" y2="13" stroke="#fff" stroke-width="1.8"/></svg>
    <span>Wat voor werk wil ik doen?</span>
  </div>
  <div class="abs search-field search-branch">
    <span>Branche</span>
    <svg width="10" height="6" viewBox="0 0 10 6"><path d="M0 0h10L5 6z" fill="#fff"/></svg>
  </div>
  <div class="abs search-field search-submit">Zoeken</div>
</header>

<section>
  <div class="abs featured"></div>
  <h2 class="abs section-title" style="top:406px">Uitgelichte vacatures</h2>

  <article class="abs job-card" style="left:208px">
    <div class="job-title">Timmerman</div>
    <span class="job-badge">Populair</span>
    <div class="job-place">Eindhoven</div>
    <p class="job-text">Lorem ipsum dolor sit amet, consectetur adipisicing elit, sed do eiusmod tempor incididunt ut labore et dolore magna aliqua. Ut enim ad minim veniam, quis nostrud exercitation ullamco laboris nisi ut aliquip ex ea commodo consequat. Duis aute</p>
  </article>
  <article class="abs job-card" style="left:408px">
    <div class="job-title is-tagged">Lasser weekenddienst<br>bij Zuidhorn</div>
    <div class="job-place">Amsterdam</div>
    <p class="job-text">Lorem ipsum dolor sit amet, consectetur adipisicing elit, sed do eiusmod tempor incididunt ut labore et dolore magna aliqua. Ut enim ad minim veniam, quis nostrud exercitation ullamco laboris nisi ut aliquip ex ea commodo consequat.</p>
  </article>
  <article class="abs job-card" style="left:608px">
    <div class="job-title">Junior webdesigner</div>
    <div class="job-place">Utrecht</div>
    <p class="job-text">Lorem ipsum dolor sit amet, consectetur adipisicing elit, sed do eiusmod tempor incididunt ut labore et dolore magna aliqua. Ut enim ad minim veniam, quis nostrud exercitation ullamco laboris nisi ut aliquip ex ea commodo consequat. Duis aute</p>
  </article>
  <article class="abs job-card" style="left:808px">
    <div class="job-title">PHP-programmeur</div>
    <div class="job-place">Groningen</div>
    <p class="job-text">Lorem ipsum dolor sit amet, consectetur adipisicing elit, sed do eiusmod tempor incididunt ut labore et dolore magna aliqua. Ut enim ad minim veniam, quis nostrud exercitation ullamco laboris nisi ut aliquip ex ea commodo consequat.</p>
  </article>

  <div class="abs job-more" style="left:244px"><span class="btn-more">Lees meer</span><span class="btn-arrow"></span></div>
  <div class="abs job-more" style="left:444px"><span class="btn-more">Lees meer</span><span class="btn-arrow"></span></div>
  <div class="abs job-more" style="left:644px"><span class="btn-more">Lees meer</span><span class="btn-arrow"></span></div>
  <div class="abs job-more" style="left:844px"><span class="btn-more">Lees meer</span><span class="btn-arrow"></span></div>

  <div class="abs all-jobs">Alle vacatures</div>
</section>

<section>
  <h2 class="abs section-title" style="top:800px">Over WerkKring</h2>
  <div class="abs photo photo-tech" role="img" aria-label="Foto van een technische werkomgeving in blauwe tinten"></div>
  <div class="abs photo photo-side" role="img" aria-label="Foto van collega's aan het werk op kantoor"></div>
  <div class="abs photo photo-main" role="img" aria-label="Foto van een lachende medewerker achter een computer"></div>
  <div class="abs about-text">
    <p>Lorem ipsum dolor sit amet, consectetur adipisicing elit, sed do eiusmod tempor incididunt ut labore et dolore magna aliqua. Ut enim ad minim veniam, quis nostrud exercitation ullamco laboris nisi ut aliquip ex ea commodo consequat. Duis aute irure dolor in reprehenderit in voluptate velit esse cillum dolore eu fugiat nulla pariatur. Excepteur sint occaecat cupidatat non proident, sunt in culpa qui officia deserunt mollit anim id est laborum. Sed ut perspiciatis unde omnis iste natus error sit voluptatem accusantium doloremque.</p>
    <p>Veritatis et quasi architecto beatae vitae dicta sunt explicabo. Nemo enim ipsam voluptatem quia voluptas sit aspernatur aut odit aut fugit, sed quia consequuntur magni dolores eos qui ratione voluptatem sequi nesciunt. Neque porro quisquam est, qui dolorem ipsum quia dolor sit amet, consectetur, adipisci velit, sed quia non numquam eius modi tempora incidunt ut labore et dolore magnam aliquam quaerat voluptatem.</p>
  </div>
</section>

<section>
  <div class="abs newsletter" role="img" aria-label="Foto van een lachende vrouw met een telefoon, in warme zachte tinten"></div>
  <div class="abs newsletter-shade"></div>
  <h2 class="abs newsletter-title">Aanmelden voor de nieuwsbrief</h2>
  <div class="abs newsletter-input">Je e-mailadres</div>
  <div class="abs newsletter-submit"><span class="btn-more">Aanmelden</span><span class="btn-arrow"></span></div>
</section>

<section>
  <h2 class="abs section-title" style="top:1518px">Vrije teaser om zelf in te vullen</h2>
  <p class="abs teaser-col" style="left:208px">Lorem ipsum dolor sit amet, consectetur adipisicing elit, sed do eiusmod tempor incididunt ut labore et dolore magna aliqua. Ut enim ad minim veniam, quis nostrud exercitation ullamco laboris nisi ut aliquip ex ea commodo consequat. Duis aute irure dolor in reprehenderit in voluptate velit esse cillum dolore eu fugiat nulla pariatur. Excepteur sint occaecat non proident.</p>
  <p class="abs teaser-col" style="left:608px">Perspiciatis unde omnis iste natus error sit voluptatem accusantium doloremque laudantium, totam rem aperiam, eaque ipsa quae ab illo inventore veritatis et quasi architecto beatae vitae dicta sunt explicabo. Nemo enim ipsam voluptatem quia voluptas sit aspernatur aut odit aut fugit, sed quia magni dolores eos qui ratione. Neque porro quisquam est.</p>
</section>

<section>
  <h2 class="abs section-title" style="top:1664px">Wie zijn wij?</h2>
  <div class="abs team-band"></div>
  <div class="abs member member-dark" style="left:239px;top:1780px"></div>
  <div class="abs member member-photo-a" role="img" aria-label="Portretfoto van een teamlid" style="left:539px;top:1780px"></div>
  <div class="abs member member-photo-b" role="img" aria-label="Portretfoto van een teamlid" style="left:839px;top:1780px"></div>
  <div class="abs member-name">Sanne Bakker</div>
  <div class="abs member-role">Recruiter</div>
  <div class="abs member-socials"><span class="social-dot"></span><span class="social-dot"></span><span class="social-dot"></span></div>
</section>

<section>
  <h2 class="abs section-title" style="top:1996px">Met wie werkt WerkKring samen?</h2>
  <div class="abs partner" style="left:412px;top:2060px"><span class="partner-frame"></span><span class="partner-name">Vensterra</span></div>
  <div class="abs partner" style="left:552px;top:2060px"><span class="partner-frame"></span><span class="partner-name">Norbix</span></div>
  <div class="abs partner" style="left:692px;top:2060px"><span class="partner-frame"></span><span class="partner-name">Kelvo</span></div>
  <div class="abs partner" style="left:342px;top:2130px"><span class="partner-frame"></span><span class="partner-name">Hapra</span></div>
  <div class="abs partner" style="left:482px;top:2130px"><span class="partner-frame"></span><span class="partner-name">Sorin</span></div>
  <div class="abs partner" style="left:622px;top:2130px"><span class="partner-frame"></span><span class="partner-name">Acora</span></div>
  <div class="abs partner" style="left:762px;top:2130px"><span class="partner-frame"></span><span class="partner-name">Azeli</span></div>
  <div class="abs partner" style="left:412px;top:2200px"><span class="partner-frame"></span><span class="partner-name">Pomelo</span></div>
  <div class="abs partner" style="left:552px;top:2200px"><span class="partner-frame"></span><span class="partner-name">Samhera</span></div>
  <div class="abs partner" style="left:692px;top:2200px"><span class="partner-frame"></span><span class="partner-name">Huvento</span></div>
</section>

<footer>
  <div class="abs footer"></div>
  <div class="abs footer-col" style="left:208px">
    <h3>Over ons</h3>
    <p>Aliquam luctus nulla augue, quis aliquet leo porta tincidunt. Donec turpis tellus, luctus eu neque lobortis, eleifend facilisis mauris. Aenean sodales sapien diam. Morbi dignissim nibh eu tempor pharetra. Nam ac nibh porttitor.</p>
  </div>
  <div class="abs footer-col" style="left:408px">
    <h3>RSS</h3>
    <p>Praesent quis Donec in accumsan <span class="underline">porta tincidunt. Donec turpis tellus, luctus eu neque</span></p>
    <p style="margin-top:12px">et rhoncus lectus erat pellentes que odio. In commodo</p>
  </div>
  <div class="abs footer-col" style="left:608px">
    <h3>Vacatures</h3>
    <p class="underline">Lorem ipsum dolor sit amet, consectetur adipisicing elit, sed do eiusmod tempor incididunt ut labore et dolore magna aliqua. Ut enim ad minim veniam, aliquip ex ea commodo</p>
  </div>
  <div class="abs footer-col" style="left:808px">
    <h3>Contact</h3>
    <p>WerkKring B.V.<br>Lindengracht 212B<br>1015 KM Amsterdam</p>
    <div class="footer-socials"><span class="social-dot"></span><span class="social-dot"></span><span class="social-dot"></span></div>
  </div>
</footer>

</body>
</html>
```